Morvik Construction Business Card

I need a business card design for my company.
We are a construction/machinery company.
I would like to see my logo on the front of the card and my details on the other side
I would like the card to be black or dark grey in colour,with my logo as i send it or modified with a lighter blue colour
I would like to see the design kept fairly simple,but eye catching at the same time
Industry/Entity Type
Business
Colors
00a990
1b1b1b
000000
474747
ececec

```html
<!DOCTYPE html>
<html lang="en">
<head>
<meta charset="utf-8">
<title>Morvik Construction Business Card</title>
<link rel="stylesheet" href="https://fonts.googleapis.com/css2?family=Arimo:wght@400;700&display=swap">
<style>
  :root {
    --backdrop: #d9d6d2;
    --card: #262626;
    --accent: #29abe2;
    --ink-light: #ffffff;
    --shadow: rgba(0, 0, 0, 0.35);
  }
  * { margin: 0; padding: 0; box-sizing: border-box; }
  html, body {
    width: 1200px;
    height: 1000px;
    overflow: hidden;
    background: var(--backdrop);
    font-family: "Arimo", Arial, sans-serif;
  }
  .card {
    position: absolute;
    left: 265px;
    width: 666px;
    height: 397px;
    background: var(--card);
    box-shadow: 0 6px 14px var(--shadow);
  }
  .card--front { top: 73px; }
  .card--back { top: 532px; }

  .wordmark {
    position: absolute;
    left: 0; right: 0;
    top: 150px;
    text-align: center;
    color: var(--accent);
    font-weight: 700;
    line-height: 1;
  }
  .wordmark__name { display: block; font-size: 84px; letter-spacing: 4px; }
  .wordmark__trade { display: block; font-size: 30px; letter-spacing: 6px; margin-top: 10px; }

  .identity {
    position: absolute;
    right: 363px;
    top: 171px;
    text-align: right;
  }
  .identity__name {
    color: var(--accent);
    font-weight: 700;
    font-size: 21px;
    letter-spacing: 0.3px;
  }
  .identity__role {
    color: var(--ink-light);
    font-size: 15px;
    margin-top: 6px;
  }
  .divider {
    position: absolute;
    left: 328px;
    top: 168px;
    width: 2px;
    height: 61px;
    background: var(--ink-light);
  }
  .contacts {
    position: absolute;
    left: 352px;
    top: 164px;
    list-style: none;
  }
  .contacts li {
    display: flex;
    align-items: center;
    height: 22.5px;
    color: var(--ink-light);
    font-size: 15.5px;
  }
  .contacts svg { width: 14px; height: 14px; margin-right: 12px; fill: var(--accent); }
  .address {
    position: absolute;
    left: 0; right: 0;
    top: 337px;
    display: flex;
    justify-content: center;
    align-items: center;
    color: var(--ink-light);
    font-size: 16px;
    letter-spacing: 0.3px;
  }
  .address svg { width: 14px; height: 19px; margin-right: 9px; fill: var(--accent); }
</style>
</head>
<body>
  <section class="card card--front">
    <div class="wordmark">
      <span class="wordmark__name">MORVIK</span>
      <span class="wordmark__trade">CONSTRUCTION</span>
    </div>
  </section>

  <section class="card card--back">
    <div class="identity">
      <div class="identity__name">DANE HOLLOWAY</div>
      <div class="identity__role">Director of operations</div>
    </div>
    <div class="divider"></div>
    <ul class="contacts">
      <li>
        <svg viewBox="0 0 16 16" aria-hidden="true"><path d="M2 6c0-2 3-3 6-3s6 1 6 3v1h-3V5.5H5V7H2zM4 8h8l2 5H2z"/></svg>
        + 999 999 9999
      </li>
      <li>
        <svg viewBox="0 0 16 16" aria-hidden="true"><path d="M1 3h14v1L8 9 1 4zM1 5.5l7 5 7-5V13H1z"/></svg>
        info@morvikconstruction.com.au
      </li>
      <li>
        <svg viewBox="0 0 16 16" aria-hidden="true"><path d="M8 1a7 7 0 1 0 0 14A7 7 0 0 0 8 1zm0 1.6a5.4 5.4 0 0 1 4.6 2.6H10L9 6.5 7 5.5 5 7l1 2 2 .5.5 2L7 13.3A5.4 5.4 0 0 1 2.6 8 5.4 5.4 0 0 1 8 2.6z"/></svg>
        www.morvikconstruction.com.au
      </li>
    </ul>
    <div class="address">
      <svg viewBox="0 0 14 19" aria-hidden="true"><path d="M7 0a7 7 0 0 0-7 7c0 5 7 12 7 12s7-7 7-12a7 7 0 0 0-7-7zm0 4a3 3 0 1 1 0 6 3 3 0 0 1 0-6z"/></svg>
      2190 Ridgeway Drive, Fernhill, VA 24811
    </div>
  </section>
</body>
</html>
```